InfoGraphic for Security Pyramid

I've created an infographic that I would like to be redone more professionally. you can see the page in this powerpoint called the pyramid of security. What I'd like done is to replace the background graphic with a new icon in a cartoony format like the one behind end point protection as an example (thats a stock photo).

Target Market(s)

Business Owners

Font styles to use
Sans Serif

Colors
ec1f27
0355a3
f37122

Requirements
Must have
• Consistent images, text must be editable.

```html
<!DOCTYPE html>
<html lang="en">
<head>
<meta charset="utf-8">
<title>Pyramid of Security</title>
<link rel="stylesheet" href="https://fonts.googleapis.com/css2?family=Roboto:wght@500;700&family=Bebas+Neue&display=swap">
<style>
  :root {
    --brand-red: #ec1f27;
    --brand-blue: #0355a3;
    --brand-orange: #f37122;
    --paper: #ffffff;
    --label: #ffffff;
  }
  html, body {
    margin: 0;
    padding: 0;
    width: 1200px;
    height: 1200px;
    overflow: hidden;
    background: var(--paper);
  }
  .canvas {
    display: block;
    width: 1200px;
    height: 1200px;
  }
  .tier-red { fill: var(--brand-red); }
  .tier-blue { fill: var(--brand-blue); }
  .tier-orange { fill: var(--brand-orange); }
  .tile-label {
    font-family: "Roboto", Arial, sans-serif;
    font-weight: 700;
    font-size: 22px;
    fill: var(--label);
    text-anchor: middle;
    filter: drop-shadow(1px 2px 1px rgba(0,0,0,0.35));
  }
  .tile-icon {
    fill: #ffffff;
    fill-opacity: 0.2;
  }
  .brand-name {
    font-family: "Roboto", Arial, sans-serif;
    font-weight: 700;
    font-size: 40px;
    fill: var(--brand-blue);
  }
  .brand-tagline {
    font-family: "Roboto", Arial, sans-serif;
    font-weight: 500;
    font-size: 16px;
    letter-spacing: 0.5px;
    fill: var(--brand-orange);
  }
  .poster-title {
    font-family: "Bebas Neue", "Oswald", sans-serif;
    font-size: 100px;
    fill: var(--brand-blue);
    text-anchor: middle;
  }
</style>
</head>
<body>
<svg class="canvas" viewBox="0 0 1200 1200" xmlns="http://www.w3.org/2000/svg">
  <defs>
    <clipPath id="pyramid-outline">
      <polygon points="600,78 1176,1071 24,1071"/>
    </clipPath>
  </defs>

  <g class="brand">
    <text class="brand-name" x="64" y="114">Kestrel Systems</text>
    <text class="brand-tagline" x="66" y="146">Plan Protect Prosper</text>
  </g>

  <g class="pyramid" clip-path="url(#pyramid-outline)">
    <rect class="tier-red" x="0" y="78" width="1200" height="218"/>
    <rect class="tier-blue" x="0" y="305" width="595" height="185"/>
    <rect class="tier-blue" x="603" y="305" width="597" height="185"/>
    <rect class="tier-orange" x="0" y="498" width="492" height="184"/>
    <rect class="tier-orange" x="500" y="498" width="203" height="184"/>
    <rect class="tier-orange" x="711" y="498" width="489" height="184"/>
    <rect class="tier-red" x="0" y="690" width="397" height="185"/>
    <rect class="tier-red" x="405" y="690" width="189" height="185"/>
    <rect class="tier-red" x="602" y="690" width="193" height="185"/>
    <rect class="tier-red" x="803" y="690" width="397" height="185"/>
    <rect class="tier-blue" x="0" y="883" width="283" height="188"/>
    <rect class="tier-blue" x="291" y="883" width="202" height="188"/>
    <rect class="tier-blue" x="501" y="883" width="202" height="188"/>
    <rect class="tier-blue" x="711" y="883" width="196" height="188"/>
    <rect class="tier-blue" x="915" y="883" width="285" height="188"/>
  </g>

  <g class="tile-icons">
    <rect class="tile-icon" x="558" y="170" width="76" height="76" rx="12" role="img" aria-label="Icon of a trainer with megaphone and audience"/>
    <rect class="tile-icon" x="476" y="342" width="76" height="76" rx="12" role="img" aria-label="Globe icon with shield"/>
    <rect class="tile-icon" x="646" y="337" width="76" height="76" rx="12" role="img" aria-label="Radar scanning icon"/>
    <rect class="tile-icon" x="370" y="533" width="76" height="76" rx="12" role="img" aria-label="Iceberg icon"/>
    <rect class="tile-icon" x="562" y="533" width="76" height="76" rx="12" role="img" aria-label="Circular arrows icon"/>
    <rect class="tile-icon" x="758" y="537" width="76" height="76" rx="12" role="img" aria-label="ID card icon"/>
    <rect class="tile-icon" x="260" y="725" width="76" height="76" rx="12" role="img" aria-label="Brick wall with shield icon"/>
    <rect class="tile-icon" x="464" y="725" width="76" height="76" rx="12" role="img" aria-label="Phone with shield icon"/>
    <rect class="tile-icon" x="657" y="721" width="76" height="76" rx="12" role="img" aria-label="Umbrella over computers icon"/>
    <rect class="tile-icon" x="846" y="729" width="76" height="76" rx="12" role="img" aria-label="Bucket with down arrow icon"/>
    <rect class="tile-icon" x="148" y="925" width="76" height="76" rx="12" role="img" aria-label="Upload tray icon"/>
    <rect class="tile-icon" x="364" y="925" width="76" height="76" rx="12" role="img" aria-label="Padlock with password field icon"/>
    <rect class="tile-icon" x="574" y="921" width="76" height="76" rx="12" role="img" aria-label="Database with restore arrow icon"/>
    <rect class="tile-icon" x="768" y="917" width="76" height="76" rx="12" role="img" aria-label="Laptop with shield icon"/>
    <rect class="tile-icon" x="978" y="917" width="76" height="76" rx="12" role="img" aria-label="Envelope with shield icon"/>
  </g>

  <g class="tile-labels">
    <text class="tile-label" x="600" y="282">User Training</text>

    <text class="tile-label" x="499" y="468">Web Filtering</text>
    <text class="tile-label" x="694" y="458">Continuous</text>
    <text class="tile-label" x="694" y="481">Scanning</text>

    <text class="tile-label" x="388" y="662">Threat Intel</text>
    <text class="tile-label" x="601" y="651">Asset</text>
    <text class="tile-label" x="601" y="674">Management</text>
    <text class="tile-label" x="812" y="660">Minimize Admin</text>

    <text class="tile-label" x="287" y="856">Next Gen Firewall</text>
    <text class="tile-label" x="499" y="856">Mobile Security</text>
    <text class="tile-label" x="692" y="848">Cyber</text>
    <text class="tile-label" x="692" y="871">Insurance</text>
    <text class="tile-label" x="884" y="856">Logging</text>

    <text class="tile-label" x="183" y="1045">Updating</text>
    <text class="tile-label" x="400" y="1045">Passwords</text>
    <text class="tile-label" x="607" y="1045">Backups</text>
    <text class="tile-label" x="810" y="1041">Endpoint</text>
    <text class="tile-label" x="810" y="1064">Protection</text>
    <text class="tile-label" x="1022" y="1042">Email Security</text>
  </g>

  <text class="poster-title" x="602" y="1176" textLength="656" lengthAdjust="spacingAndGlyphs">PYRAMID OF SECURITY</text>
</svg>
</body>
</html>
```